Construction Company

Design a clutter free business card, it can be double-sided utilizing the logo for BDN Ltd simple with all relevant contact information.

Please also a letterhead design to function for the purposes of invoicing, all mail requirements, with header to be distinctive while the footer ties page together and incorporates all necessary information.

For now, please use generic / dummy text and when a winner is selected, I will disclose the contact information.

Hi Designers! Please read the updated brief which includes the design of a business card and letterhead. Thank you!

```html
<!DOCTYPE html>
<html lang="en">
<head>
<meta charset="utf-8">
<title>BDN Ltd — Letterhead and Business Cards</title>
<link rel="stylesheet" href="https://fonts.googleapis.com/css2?family=Roboto:wght@400&family=Roboto+Condensed:wght@400&family=EB+Garamond:wght@500&display=swap">
<style>
  :root{
    --gold:#b08f33;
    --gold-soft:#e6d7b0;
    --navy:#1f2f7a;
    --ink:#333333;
    --paper:#f6f6f4;
    --card-white:#f8f8f6;
    --backdrop:#d9d9d9;
  }
  *{margin:0;padding:0;box-sizing:border-box}
  html,body{width:1200px;height:800px;overflow:hidden}
  body{background:var(--backdrop);position:relative;font-family:"Roboto Condensed","Roboto",sans-serif;color:var(--ink)}

  /* Letterhead */
  .letterhead{position:absolute;left:203px;top:87px;width:443px;height:627px;background:var(--paper);box-shadow:0 6px 18px rgba(0,0,0,.18);overflow:hidden}
  .letterhead__ornament{position:absolute;right:0;top:0;width:131px;height:204px;
    background:radial-gradient(ellipse at 85% 20%,var(--gold) 0%,rgba(176,143,51,.75) 38%,rgba(230,215,176,.5) 65%,rgba(246,246,244,0) 85%)}
  .letterhead__salutation{position:absolute;left:22px;top:66px;font-size:10px}
  .letterhead__body{position:absolute;left:22px;top:129px;width:371px;font-size:10px;line-height:16.2px;text-align:justify}
  .letterhead__body p{margin-bottom:16px}
  .letterhead__footer{position:absolute;left:14px;right:18px;bottom:14px;display:flex;justify-content:space-between;align-items:flex-end}
  .brand-name{font-family:"EB Garamond",serif;font-weight:500;color:var(--navy);letter-spacing:-.5px;white-space:nowrap}
  .letterhead__footer .brand-name{font-size:27px;line-height:1}
  .letterhead__contact{font-family:"Roboto",sans-serif;font-size:7.4px;line-height:11px;color:var(--ink);font-style:normal}
  .contact-row{display:flex;align-items:center;gap:8px}
  .contact-item{display:inline-flex;align-items:center;gap:3px;white-space:nowrap}
  .icon{display:inline-block;width:6px;height:6px;border-radius:50%;background:var(--navy)}

  /* Business cards */
  .card{position:absolute;width:191px;height:117px;overflow:hidden;box-shadow:0 5px 14px rgba(0,0,0,.2)}
  .card--back{left:834px;top:143px;background:var(--gold)}
  .card--front{left:832px;top:319px;background:var(--card-white)}
  .card__ornament{position:absolute;right:0;top:0;width:64px;height:106px}
  .card--back .card__ornament{background:radial-gradient(ellipse at 70% 35%,rgba(255,255,255,.55) 0%,rgba(255,255,255,.25) 45%,rgba(176,143,51,0) 80%)}
  .card--front .card__ornament{background:radial-gradient(ellipse at 70% 30%,var(--gold) 0%,rgba(176,143,51,.55) 45%,rgba(248,248,246,0) 82%)}
  .card__address{position:absolute;left:5px;bottom:8px;font-family:"Roboto",sans-serif;font-size:5.6px;color:#fff;white-space:nowrap}
  .card__logo{position:absolute;left:6px;top:7px;font-size:22px;line-height:1}
  .card__name{position:absolute;left:7px;top:54px;font-family:"EB Garamond",serif;font-weight:500;color:var(--navy);font-size:12px}
  .card__name small{font-size:6px}
  .card__contact{position:absolute;left:6px;bottom:5px;font-family:"Roboto",sans-serif;font-size:5.6px;line-height:8px;color:var(--navy);display:grid;grid-template-columns:auto auto;column-gap:8px}
  .card__contact .icon{width:5px;height:5px}
</style>
</head>
<body>

<section class="letterhead" aria-label="Letterhead">
  <div class="letterhead__ornament" role="img" aria-label="Gold floral petal decoration in the top right corner"></div>
  <p class="letterhead__salutation">Dear</p>
  <div class="letterhead__body">
    <p>Ah, business letter format-there are block formats, and indented formats, and modified block formats . . . and who knows what others. To simplify matters, we’re demonstrating the block format on this page, one of the two most common formats. For authoritative advice about all the variations, we highly recommend The Harlow Style Handbook, 9th ed. (New York: Westbrook Press, 2001), a great reference tool for workplace communications. There seems to be no consensus about such fine points as whether to skip a line after your return address and before the date: some guidelines suggest that you do; others do not. Let’s hope that your business letter succeeds no matter which choice you make!</p>
    <p>When you use the block form to write a business letter, all the information is typed flush left, with one-inch margins all around. First provide your own address, then skip a line and provide the date, then skip one more line and provide the inside address of the party to whom the letter is addressed. If you are using letterhead that already provides your address, do not retype that information; just begin with the date. For formal letters, avoid abbreviations where possible.</p>
    <p>Skip another line before the salutation, which should be followed by a colon. Then write the body of your letter as illustrated here, with no indentation at the beginnings of paragraphs. Skip lines between paragraphs.</p>
    <p>After writing the body of the letter, type the closing, followed by a comma, leave 3 blank lines, then type your name and title (if applicable), all flush left. Sign the letter in the blank space above your typed name. Now doesn’t that look professional?</p>
  </div>
  <footer class="letterhead__footer">
    <div class="brand-name">BDN Ltd</div>
    <address class="letterhead__contact">
      <div>123, dummy rd., dummy state, dummy country</div>
      <div class="contact-row">
        <span class="contact-item"><span class="icon"></span>47 310 552</span>
        <span class="contact-item"><span class="icon"></span>info@bdn.com</span>
        <span class="contact-item"><span class="icon"></span>www.bdn.com</span>
      </div>
    </address>
  </footer>
</section>

<section class="card card--back" aria-label="Business card, back">
  <div class="card__ornament" role="img" aria-label="White floral petal decoration"></div>
  <p class="card__address">123, dummy rd., dummy state, dummy country</p>
</section>

<section class="card card--front" aria-label="Business card, front">
  <div class="card__ornament" role="img" aria-label="Gold floral petal decoration"></div>
  <div class="card__logo brand-name">BDN Ltd</div>
  <p class="card__name">John Doe, <small>ceo</small></p>
  <div class="card__contact">
    <span class="contact-item"><span class="icon"></span>18 204 639</span>
    <span class="contact-item"><span class="icon"></span>info@bdn.com</span>
    <span class="contact-item"><span class="icon"></span>47 310 552</span>
    <span class="contact-item"><span class="icon"></span>www.bdn.com</span>
  </div>
</section>

</body>
</html>
```